The Maplewood Learning House Web Page

We need a web design for our Day Care Center based in Brandon, Florida. We are targeting child care and educational services to middle class parents, specially the mother. We would like to see designs that matches attached logo mark. The final design should communicate higher standards for day care and educational services.

Middle class parents in the State of Florida

```html
<!DOCTYPE html>
<html lang="en">
<head>
<meta charset="utf-8">
<title>The Maplewood Learning House</title>
<link rel="stylesheet" href="https://fonts.googleapis.com/css2?family=Dosis:wght@400;500;600;700&family=Open+Sans:wght@400;600;700&family=Caveat:wght@400&display=swap">
<style>
:root{
  --navy:#051a3a;
  --navy-mid:#1c3a66;
  --navy-btn:#12315c;
  --blue-band:#27497a;
  --gold:#e2a33a;
  --accent:#e8953a;
  --ink:#333a44;
  --ink-soft:#555b63;
  --rule:#dcdfe3;
  --footer:#1f1f1f;
  --footer-field:#2d2d2d;
  --white:#ffffff;
}
*{margin:0;padding:0;box-sizing:border-box}
html,body{width:1200px;height:2219px;overflow:hidden}
body{position:relative;background:var(--white);font-family:"Open Sans",Arial,sans-serif;color:var(--ink)}
.abs{position:absolute}

/* header */
.site-header{position:absolute;left:0;top:0;width:1200px;height:111px;background:var(--navy);z-index:3}
.nav-link{position:absolute;top:64px;font-size:11px;color:var(--white);letter-spacing:.3px;text-transform:uppercase;font-family:Arial,Helvetica,sans-serif}
.nav-link.is-active{color:var(--gold)}
.brand{position:absolute;left:535px;top:24px;width:130px;height:130px;border-radius:50%;background:var(--navy);z-index:4;display:flex;align-items:center;justify-content:center;text-align:center}
.brand-name{font-family:"Dosis",sans-serif;font-weight:600;font-size:15px;line-height:1.15;color:var(--gold);text-transform:uppercase;width:100px}
.dropdown{position:absolute;left:222px;top:112px;width:148px;height:104px;background:#7f95b6;z-index:4;padding:6px 10px;box-shadow:0 3px 6px rgba(0,0,0,.25)}
.dropdown a{display:block;font-size:11px;color:#0b1a33;font-family:Arial,sans-serif;height:33px;line-height:30px;border-bottom:1px solid rgba(255,255,255,.35)}
.dropdown a:last-child{border-bottom:none}

/* hero */
.hero{position:absolute;left:0;top:111px;width:1200px;height:519px;background:linear-gradient(100deg,#e8e3dc 0%,#d9cfc4 35%,#bfa48c 60%,#d7a07f 75%,#efe6dc 100%)}
.hero-title{position:absolute;left:98px;top:336px;font-family:"Dosis",sans-serif;font-weight:600;font-size:52px;color:var(--white);letter-spacing:1px;text-shadow:0 2px 4px rgba(0,0,0,.25)}
.hero-sub{position:absolute;left:99px;top:404px;font-family:"Caveat",cursive;font-size:30px;color:#f6e7b8;letter-spacing:1px}
.hero-arc{position:absolute;left:296px;top:442px}
.btn{position:absolute;background:var(--navy-btn);color:var(--white);font-family:"Open Sans",sans-serif;font-weight:700;text-transform:uppercase;text-align:center;border-radius:2px;box-shadow:0 2px 3px rgba(0,0,0,.3)}
.btn-join{left:99px;top:475px;width:105px;height:36px;line-height:36px;font-size:14px}
.dots{position:absolute;left:242px;top:499px;display:flex;gap:6px}
.dots i{width:11px;height:11px;border-radius:50%;background:var(--white)}
.dots i.on{background:var(--navy-btn)}

/* section titles */
.section-title{position:absolute;left:0;width:1200px;text-align:center;font-family:"Dosis",sans-serif;font-size:22px;font-weight:500;color:#333;letter-spacing:.5px}
.title-arc{position:absolute;left:585px}
.divider{position:absolute;left:98px;width:1003px;height:1px;background:var(--rule)}
.divider::after{content:"";position:absolute;left:498px;top:-3px;width:7px;height:7px;border-radius:50%;background:#cfd3d8}

.about-text{position:absolute;left:110px;top:733px;width:980px;text-align:center;font-size:11.5px;line-height:20px;color:var(--ink-soft)}
.btn-more{left:556px;top:837px;width:91px;height:30px;line-height:30px;font-size:11px;font-weight:400}

/* services */
.services-band{position:absolute;left:0;top:1006px;width:1200px;height:208px;background:linear-gradient(90deg,#6a5046 0%,#8d6a5b 35%,#b98f7d 55%,#7d5e50 80%,#5c4338 100%)}
.services-quote{position:absolute;left:0;top:1030px;width:1200px;text-align:center;font-family:"Dosis",sans-serif;font-weight:600;font-size:30px;color:var(--white);letter-spacing:.5px}
.service{position:absolute;top:1170px;width:240px;text-align:center}
.service-icon{width:78px;height:78px;border-radius:50%;background:var(--navy-mid);margin:0 auto;display:flex;align-items:center;justify-content:center;box-shadow:0 2px 4px rgba(0,0,0,.25)}
.service h3{margin-top:20px;font-family:"Open Sans",sans-serif;font-weight:700;font-size:14px;color:#222;letter-spacing:.3px}
.service p{margin-top:8px;font-size:11.5px;line-height:19px;color:var(--ink-soft)}
.service .more{display:block;margin-top:8px;font-size:12px;font-weight:700;color:var(--navy-mid)}

/* programs */
.programs-band{position:absolute;left:0;top:1523px;width:1200px;height:297px}
.programs-photo{position:absolute;left:0;top:0;width:560px;height:297px;background:linear-gradient(90deg,#d8cfc4 0%,#e9e4dd 40%,#c7d3e2 100%)}
.programs-intro{position:absolute;left:550px;top:1553px;width:560px;font-size:11.5px;line-height:20px;color:var(--white)}
.program{position:absolute;font-size:11.5px;color:var(--white);text-transform:uppercase;display:flex;align-items:center;gap:9px}
.band-shadow{position:absolute;left:0;top:1820px;width:1200px;height:36px;background:radial-gradient(ellipse 45% 100% at 50% 0%,rgba(0,0,0,.22),rgba(0,0,0,0) 70%)}

/* footer */
.site-footer{position:absolute;left:0;top:1884px;width:1200px;height:335px;background:var(--footer)}
.footer-heading{position:absolute;top:1920px;font-family:"Open Sans",sans-serif;font-weight:700;font-size:13.5px;color:var(--white);padding-bottom:8px;width:150px;border-bottom:1px solid #3a3a3a}
.footer-links{position:absolute;left:98px;top:1969px;list-style:none}
.footer-links li{font-size:11px;line-height:20px;color:#dcdcdc}
.footer-copy{position:absolute;left:364px;top:1968px;width:375px;font-size:11px;line-height:20px;color:#dcdcdc}
.field{position:absolute;left:852px;width:249px;height:27px;background:var(--footer-field);color:#6f6f6f;font-size:10.5px;line-height:27px;padding-left:10px}
.btn-subscribe{left:852px;top:2051px;width:106px;height:30px;line-height:30px;font-size:11.5px}
.footer-rule{position:absolute;left:98px;top:2127px;width:1003px;height:1px;background:#343434}
.copyright{position:absolute;left:98px;top:2177px;font-size:11px;color:#dcdcdc}
.social{position:absolute;top:2155px;width:36px;height:36px;border-radius:50%;background:#2e2e2e}
</style>
</head>
<body>

<header class="site-header">
  <a class="nav-link" style="left:98px">Home</a>
  <a class="nav-link" style="left:163px">About</a>
  <a class="nav-link is-active" style="left:232px">Admissions</a>
  <a class="nav-link" style="left:331px">Philosophy</a>
  <a class="nav-link" style="left:432px">Programs</a>
  <a class="nav-link" style="left:689px">Services</a>
  <a class="nav-link" style="left:774px">Campuses</a>
  <a class="nav-link" style="left:866px">Franchises</a>
  <a class="nav-link" style="left:966px">Business</a>
  <a class="nav-link" style="left:1052px">Contact</a>
</header>
<div class="brand"><span class="brand-name">The Maplewood Learning House</span></div>

<nav class="dropdown">
  <a>Apply for Admission</a>
  <a>Schedule a Campus Tour</a>
  <a>Enrollment Policy</a>
</nav>

<section class="hero" role="img" aria-label="Photo of a mother reading a picture book with her young daughter in a bright living room"></section>
<h1 class="hero-title">CHILDREN ARE OUR FUTURE</h1>
<p class="hero-sub">"SHE" IS ME AND MATEO IS MY SON</p>
<svg class="hero-arc" width="36" height="10" viewBox="0 0 36 10"><path d="M2 2 Q18 12 34 2" fill="none" stroke="var(--accent)" stroke-width="2"/></svg>
<a class="btn btn-join">Join Us</a>
<div class="dots"><i></i><i></i><i class="on"></i></div>

<h2 class="section-title" style="top:660px">ABOUT US</h2>
<svg class="title-arc" style="top:692px" width="30" height="10" viewBox="0 0 30 10"><path d="M2 2 Q15 12 28 2" fill="none" stroke="var(--accent)" stroke-width="2"/></svg>
<p class="about-text">Children are our future. And one by one a difference in the world can be made if each child is given the best possible chance to reach his or her full potential. Meet Mateo. He can "perfect" but she loves Mateo and does what she can by taking time to listen to him and help him with various school related work. She likes being involved in his care and knows her role is crucial in her child's development. She feels all parents share that responsibility. But when Mateo spends hours away while she works,<br>she wants the daycare to be an extension of her own home and wants to afford him every chance to excel.</p>
<a class="btn btn-more">Read More</a>

<div class="divider" style="top:901px"></div>

<h2 class="section-title" style="top:929px">SERVICES</h2>
<svg class="title-arc" style="top:961px" width="30" height="10" viewBox="0 0 30 10"><path d="M2 2 Q15 12 28 2" fill="none" stroke="var(--accent)" stroke-width="2"/></svg>

<section class="services-band" role="img" aria-label="Photo of a young girl concentrating on schoolwork"></section>
<p class="services-quote">“ SHE BELIEVES ALL CHILDREN DESERVE A CLEAN, SAFE, HEALTHY ”</p>
<svg class="title-arc" style="top:1072px" width="30" height="10" viewBox="0 0 30 10"><path d="M2 2 Q15 12 28 2" fill="none" stroke="var(--accent)" stroke-width="2"/></svg>

<div class="service" style="left:83px">
  <div class="service-icon"><svg width="24" height="22" viewBox="0 0 24 22"><path d="M12 1 L23 11 H20 V21 H14 V14 H10 V21 H4 V11 H1 Z" fill="#fff"/></svg></div>
  <h3>HOME SCHOOL SUPPORT</h3>
  <p>There are many variations of passages<br>Lorem Ipsum available</p>
  <span class="more">MORE &nbsp;›</span>
</div>
<div class="service" style="left:349px">
  <div class="service-icon"><svg width="22" height="22" viewBox="0 0 22 22"><path d="M5 2 H19 L16 20 H2 Z" fill="none" stroke="#fff" stroke-width="2.2"/><path d="M7 7 H15 M6 11 H14" stroke="#fff" stroke-width="1.8"/></svg></div>
  <h3>SCHOOL READINESS PROVIDER</h3>
  <p>There are many variations of passages<br>Lorem Ipsum available</p>
  <span class="more">MORE &nbsp;›</span>
</div>
<div class="service" style="left:615px">
  <div class="service-icon"><svg width="20" height="22" viewBox="0 0 20 22"><circle cx="10" cy="6" r="5" fill="#fff"/><path d="M1 21 Q1 12 10 12 Q19 12 19 21 Z" fill="#fff"/></svg></div>
  <h3>VOLUNTARY PRE-K (VPK)</h3>
  <p>There are many variations of passages<br>Lorem Ipsum available</p>
  <span class="more">MORE &nbsp;›</span>
</div>
<div class="service" style="left:877px">
  <div class="service-icon"><svg width="26" height="24" viewBox="0 0 26 24"><circle cx="9" cy="13" r="6" fill="none" stroke="#fff" stroke-width="3.5" stroke-dasharray="3 1.7"/><circle cx="9" cy="13" r="2" fill="#fff"/><circle cx="20" cy="6" r="4" fill="none" stroke="#fff" stroke-width="2.5" stroke-dasharray="2 1.3"/><circle cx="20" cy="19" r="3" fill="none" stroke="#fff" stroke-width="2"/></svg></div>
  <h3>ENRICHMENT SERVICES</h3>
  <p>There are many variations of passages<br>Lorem Ipsum available</p>
  <span class="more">MORE &nbsp;›</span>
</div>

<div class="divider" style="top:1400px"></div>

<h2 class="section-title" style="top:1442px">PROGRAMS</h2>
<svg class="title-arc" style="top:1474px" width="30" height="10" viewBox="0 0 30 10"><path d="M2 2 Q15 12 28 2" fill="none" stroke="var(--accent)" stroke-width="2"/></svg>

<section class="programs-band">
  <div class="programs-photo" role="img" aria-label="Photo of a teacher helping a boy write at his desk"></div>
  <svg class="abs" style="left:0;top:0" width="1200" height="297" viewBox="0 0 1200 297">
    <defs><linearGradient id="bandBlue" x1="0" y1="0" x2="0" y2="1"><stop offset="0" stop-color="#2c5185"/><stop offset="1" stop-color="#0a1f42"/></linearGradient></defs>
    <path d="M503 0 H1200 V297 H500 Q410 230 425 150 Q440 50 503 0 Z" fill="url(#bandBlue)"/>
  </svg>
</section>
<p class="programs-intro">Lorem Ipsum is simply dummy text of the printing and typesetting industry. Lorem Ipsum has been the industry's standard dummy text ever since</p>

<div class="program" style="left:548px;top:1633px"><svg width="14" height="14" viewBox="0 0 14 14"><circle cx="7" cy="7" r="7" fill="#fff"/><path d="M3.5 7 L6 9.5 L10.5 4.5" fill="none" stroke="var(--navy-mid)" stroke-width="1.8"/></svg>Children from 1 – 2 years</div>
<div class="program" style="left:548px;top:1676px"><svg width="14" height="14" viewBox="0 0 14 14"><circle cx="7" cy="7" r="7" fill="#fff"/><path d="M3.5 7 L6 9.5 L10.5 4.5" fill="none" stroke="var(--navy-mid)" stroke-width="1.8"/></svg>Children from 2 – 3 years</div>
<div class="program" style="left:548px;top:1719px"><svg width="14" height="14" viewBox="0 0 14 14"><circle cx="7" cy="7" r="7" fill="#fff"/><path d="M3.5 7 L6 9.5 L10.5 4.5" fill="none" stroke="var(--navy-mid)" stroke-width="1.8"/></svg>Children from 3 – 4 years</div>
<div class="program" style="left:548px;top:1762px"><svg width="14" height="14" viewBox="0 0 14 14"><circle cx="7" cy="7" r="7" fill="#fff"/><path d="M3.5 7 L6 9.5 L10.5 4.5" fill="none" stroke="var(--navy-mid)" stroke-width="1.8"/></svg>Children from 4 - 5 years</div>
<div class="program" style="left:832px;top:1633px"><svg width="14" height="14" viewBox="0 0 14 14"><circle cx="7" cy="7" r="7" fill="#fff"/><path d="M3.5 7 L6 9.5 L10.5 4.5" fill="none" stroke="var(--navy-mid)" stroke-width="1.8"/></svg>1s grade</div>
<div class="program" style="left:832px;top:1676px"><svg width="14" height="14" viewBox="0 0 14 14"><circle cx="7" cy="7" r="7" fill="#fff"/><path d="M3.5 7 L6 9.5 L10.5 4.5" fill="none" stroke="var(--navy-mid)" stroke-width="1.8"/></svg>2nd grade</div>
<div class="program" style="left:832px;top:1719px"><svg width="14" height="14" viewBox="0 0 14 14"><circle cx="7" cy="7" r="7" fill="#fff"/><path d="M3.5 7 L6 9.5 L10.5 4.5" fill="none" stroke="var(--navy-mid)" stroke-width="1.8"/></svg>3rd grade</div>
<div class="program" style="left:832px;top:1762px"><svg width="14" height="14" viewBox="0 0 14 14"><circle cx="7" cy="7" r="7" fill="#fff"/><path d="M3.5 7 L6 9.5 L10.5 4.5" fill="none" stroke="var(--navy-mid)" stroke-width="1.8"/></svg>4th grade</div>
<div class="program" style="left:1004px;top:1633px"><svg width="14" height="14" viewBox="0 0 14 14"><circle cx="7" cy="7" r="7" fill="#fff"/><path d="M3.5 7 L6 9.5 L10.5 4.5" fill="none" stroke="var(--navy-mid)" stroke-width="1.8"/></svg>5th grade</div>
<div class="band-shadow"></div>

<footer class="site-footer"></footer>
<h4 class="footer-heading" style="left:98px">HOME</h4>
<ul class="footer-links">
  <li>Preferred Vendors</li>
  <li>Real Estate</li>
  <li>Business Co-Ops</li>
  <li>Career Opportunities</li>
  <li>Privacy Policy</li>
  <li>Franchise Privacy Policy</li>
</ul>
<h4 class="footer-heading" style="left:364px">CAMPUSES</h4>
<p class="footer-copy">Enter contact email and Enter Zip Code to find a Center near you. Show a map with the location. Ifschool is not available. (There is no Campus available in this area yet. Would like us to contact you once it becomes available?)</p>
<h4 class="footer-heading" style="left:852px">CONTACT US</h4>
<div class="field" style="top:1974px">Enter Your Name</div>
<div class="field" style="top:2013px">Enter Your Email</div>
<a class="btn btn-subscribe">Subscribe</a>
<div class="footer-rule"></div>
<p class="copyright">Copyrights@ Maplewoodlearninghouse.2015</p>
<span class="social" style="left:937px"></span>
<span class="social" style="left:980px"></span>
<span class="social" style="left:1022px"></span>
<span class="social" style="left:1065px"></span>

</body>
</html>
```